We currently have a good logo and we want business cards that can display our logo but also represent our industry - telecom construction - We are a construction company specializing in telecom construction such as installation of fiber optic cable throughout cities and across the country. Nationwide services
We are large enough to handle most any project yet small enough to be a flexible partner and resource.

Target Market(s)

U.S. based telecom carriers and providers

Industry/Entity Type

Construction

Contact Information for Business Card

Business cards should include our logo, phone number and website address. Also, including some information as to our core services would be good.

Colors

Designer to choose colors to be used in the design.

Requirements
Must have
• Colors based on logo
• Must use our logo
• Logo, name, email, website address, phone number
• Tovek Subterra
• Brent Dacosta
• Director of Business Development
• (913) 555-0187
• www.tovekgrid.example
Nice to have
• Construction services including:
• Small Cell Construction
• Boring/Drilling
• Plowing / Trenching
• Conduit installation
• Fiber pulling
• splicing
• building entries
• Aerial construction
• Aerial Make Ready
• Make Ready Engineering
Should not have
• We are open to ideas

```html
<!DOCTYPE html>
<html lang="en">
<head>
<meta charset="utf-8">
<title>Tovek Subterra — Business Card</title>
<link href="https://fonts.googleapis.com/css2?family=Montserrat:wght@500;700;800&display=swap" rel="stylesheet">
<style>
  :root {
    --page-bg: #d9d9db;
    --card-dark: #1b1c1e;
    --brand-blue: #1a8fe0;
    --brand-blue-light: #27a9ec;
    --back-top: #27a6e8;
    --back-bottom: #0a5fc0;
    --back-logo: #0b63c4;
    --text-light: #e6e8ea;
    --text-white: #ffffff;
    --photo-warm: #8a7a5e;
    --photo-cool: #3a4552;
  }
  * { box-sizing: border-box; margin: 0; padding: 0; }
  html, body {
    width: 1200px; height: 800px; overflow: hidden;
    background: var(--page-bg);
    font-family: "Montserrat", sans-serif;
  }
  .canvas {
    width: 1200px; height: 800px;
    display: flex; align-items: center; justify-content: center; gap: 30px;
  }
  .card {
    width: 560px; height: 320px; position: relative; overflow: hidden;
    box-shadow: 0 10px 24px rgba(0,0,0,0.22);
  }

  /* Front */
  .card-front { background: var(--card-dark); }
  .site-photo {
    position: absolute; left: 0; top: 0; width: 62%; height: 100%;
    background:
      linear-gradient(90deg, rgba(27,28,30,0) 45%, var(--card-dark) 100%),
      linear-gradient(180deg, var(--card-dark) 0%, rgba(27,28,30,0) 35%),
      linear-gradient(160deg, var(--photo-warm) 20%, var(--photo-cool) 55%, #c9ced6 80%, #9aa3ad 100%);
  }
  .front-content {
    position: absolute; left: 300px; top: 48px; right: 24px;
  }
  .brand-name {
    font-weight: 800; color: var(--brand-blue);
    font-size: 30px; letter-spacing: 0.5px; line-height: 1.05;
    display: flex; align-items: center; gap: 10px;
  }
  .brand-mark {
    width: 14px; height: 14px; background: var(--brand-blue); flex: none;
  }
  .person-name {
    margin-top: 36px; font-weight: 700; color: var(--brand-blue-light);
    font-size: 18px; text-transform: uppercase; letter-spacing: 0.3px;
  }
  .person-title {
    font-weight: 500; color: var(--text-light); font-size: 11px; margin-top: 2px;
  }
  .contact-list { list-style: none; margin-top: 18px; }
  .contact-list li {
    display: flex; align-items: center; gap: 8px;
    color: var(--text-light); font-size: 11.5px; font-weight: 500; margin-bottom: 6px;
  }
  .contact-list svg { width: 11px; height: 11px; fill: var(--brand-blue-light); flex: none; }

  /* Back */
  .card-back {
    background: linear-gradient(160deg, var(--back-top) 0%, #1b8ee0 50%, var(--back-bottom) 100%);
  }
  .back-brand {
    position: absolute; left: 34px; top: 118px;
    font-weight: 800; color: var(--back-logo);
    font-size: 40px; line-height: 1; letter-spacing: 0.5px;
    display: flex; align-items: center; gap: 12px;
  }
  .back-brand .brand-mark { width: 20px; height: 20px; background: var(--back-logo); }
  .service-list {
    position: absolute; left: 330px; top: 44px;
    list-style: none;
  }
  .service-list li {
    color: var(--text-white); font-size: 13px; font-weight: 500;
    line-height: 22px; padding-left: 16px; position: relative;
  }
  .service-list li::before {
    content: ""; position: absolute; left: 0; top: 8px;
    width: 6px; height: 6px; border-radius: 50%; background: var(--text-white);
  }
</style>
</head>
<body>
<main class="canvas">

  <section class="card card-front">
    <div class="site-photo" role="img" aria-label="Photo of a white hard hat on a construction site at sunset"></div>
    <div class="front-content">
      <div class="brand-name"><span>Tovek Subterra</span><span class="brand-mark"></span></div>
      <h1 class="person-name">Brent Dacosta</h1>
      <p class="person-title">Director of Business Development</p>
      <ul class="contact-list">
        <li>
          <svg viewBox="0 0 24 24"><path d="M6.6 10.8a15 15 0 0 0 6.6 6.6l2.2-2.2a1 1 0 0 1 1-.25 11.4 11.4 0 0 0 3.6.57 1 1 0 0 1 1 1V20a1 1 0 0 1-1 1A17 17 0 0 1 3 4a1 1 0 0 1 1-1h3.5a1 1 0 0 1 1 1c0 1.25.2 2.45.57 3.57a1 1 0 0 1-.25 1z"/></svg>
          (913) 555-0187
        </li>
        <li>
          <svg viewBox="0 0 24 24"><path d="M2 5h20v14H2z M2 5l10 8 10-8" fill="none" stroke="#27a9ec" stroke-width="2.4"/></svg>
          info@tovekgrid.example
        </li>
        <li>
          <svg viewBox="0 0 24 24"><circle cx="12" cy="12" r="10"/></svg>
          www.tovekgrid.example
        </li>
      </ul>
    </div>
  </section>

  <section class="card card-back">
    <div class="back-brand"><span>Tovek<br>Subterra</span><span class="brand-mark"></span></div>
    <ul class="service-list">
      <li>Small Cell Construction</li>
      <li>Boring/Drilling</li>
      <li>Plowing / Trenching</li>
      <li>Conduit installation</li>
      <li>Fiber pulling</li>
      <li>splicing</li>
      <li>building entries</li>
      <li>Aerial construction</li>
      <li>Aerial Make Ready</li>
      <li>Make Ready Engineering</li>
    </ul>
  </section>

</main>
</body>
</html>
```